Rice Cakes Packing Desing

We need a simple (4 color) yet colorful, atractive design for a Rice Cake polypropylene bag. We are expanding our line to include 8-10 different flavors with each bag being a different color for easy identificaction. We are starting right with the first design. We already have "sample model" (of an existing product in the usa market) upon which we believe that our design could be based on (as an idea of a simple 4 color plastic bag design), which we are including in this post. We are also including an image of Brindle Rice Cakes plastic bag that has a round front window that shows the product inside the bag, which we also would like to include in our design. We already have a brand name and a logo design. The bag's dimension is about 20cms (wide) 30cms (tall) and it will contain about 12 rice cakes inside. (I HAVE ATTACHED A COUPLE OF IMAGES OF A PRINTED POLYPROPYLENE RICE CAKES BAG FOR YOUR REFERENCE)
Updates

Project Deadline Extended
Reason: We want to provide the designers with NUTRITIONAL INFORMATION, Bar Code, Company information, Ingredients, important pointers, etc. to be incorporated into the design. We would like to provide a few more days in order to fully integrate the back & front text into the package design in order to attain a perfectly balanced and well presented package. So far we have received some very interesting and highly viable proposals and we would like to provide the designers the necessary text information in order to have a complete, fully designed, great-looking package. We feel that with the extension the final design can be completed and we can have an opportunity to review, incorporate/change/modify any details before choosing the final design. Great designs have been submitted and we will definitely choose one before the newly proposed deadline. Thanks to all!

Target Market(s)

Although the concept of RICE CAKES might very well have its origins in ASIA the idea is to create a design (logo & pack) that will convey a message to the end consumer that our brand name stands for "FRESHNESS", "HEALTHY", "NATURE'S BEST", "TOP GRAINS", "GOODNESS", in short if you consume are products "IT IS GOOD FOR YOU!" (not only for people who love oriental food). We would like to have a product image that says "Hey! This looks Healthy & Tasty" (non-fattening, yummy and good!)

When you buy a pack of GRANOLAS what do you think about? What do you believe it is that you are buying? Good, Healthy Stuff? Good Tasting? Good for you? That's the idea!

Besides Rice Cakes are super light, fluffy, crunchy and easy to digest that it makes it a great Snack for everyone! Kids & Adults!

We need the full complete design of the actual bag (where the Rice Cakes will be packed) in order to start production of the bags right.

Industry/Entity Type

Plastic

Requirements
Must have
• We already have a local company in Mexico City that makes printed polypropylene bags. They are only waiting for the bag design in order to print the 20cms x 30cms bags.
Kindly consider that on the back Nutritional Information will be needed as well as a BarCode, company information, some bullets (pointing to the most important benefits of the product), etc. We will provide all the text information.
Nice to have
• Kindly take a look at the newly uploaded images from "VORNEP" Rice Cake packages. They are a good example of how to accomplish a great looking design using only 4 colors (which saves a lot in printing costs)
Should not have
• We do NOT want to have a design that says "This is ORIENTAL food". We don't want it to appear like "Sushi Rice" or "Japanese food", etc.

```html
<!DOCTYPE html>
<html lang="en">
<head>
<meta charset="utf-8">
<title>Orvale Foods Rice Cakes – Lightly Salted Bag</title>
<link rel="stylesheet" href="https://fonts.googleapis.com/css2?family=Arimo:wght@400;700&family=EB+Garamond:ital,wght@1,500&family=Lobster+Two:ital,wght@1,400&display=swap">
<style>
  :root {
    --page: #ffffff;
    --sky: #8ad8ef;
    --sky-light: #c4ecf8;
    --sky-deep: #6fcbe8;
    --tan: #dfc2a2;
    --tan-line: #f6ead9;
    --mist: #e9ecea;
    --leaf: #c9d7b4;
    --band: #dcf0f8;
    --band-text: #5c8ea3;
    --ink: #3d3d3d;
    --ink-soft: #555555;
    --white: #ffffff;
    --amber: #e9a744;
    --grain: #e6dccb;
    --grain-dark: #a89479;
  }
  * { margin: 0; padding: 0; box-sizing: border-box; }
  html, body {
    width: 800px;
    height: 1200px;
    overflow: hidden;
    background: var(--page);
  }
  .bag-front {
    display: block;
    width: 800px;
    height: 1200px;
  }
  .brand-name {
    font-family: "Arimo", sans-serif;
    font-weight: 700;
    font-size: 22px;
    fill: var(--white);
    letter-spacing: 0.5px;
  }
  .flavor {
    font-family: "EB Garamond", serif;
    font-style: italic;
    font-weight: 500;
    font-size: 38px;
    fill: var(--ink);
  }
  .benefit {
    font-family: "Arimo", sans-serif;
    font-weight: 700;
    font-size: 7.5px;
    fill: var(--ink-soft);
    letter-spacing: 0.2px;
  }
  .gluten-free {
    font-family: "Arimo", sans-serif;
    font-size: 19px;
    fill: var(--band-text);
    letter-spacing: 0.5px;
  }
  .product-name {
    font-family: "Lobster Two", cursive;
    font-style: italic;
    fill: var(--white);
    stroke: var(--amber);
    stroke-width: 1.6px;
    paint-order: stroke fill;
  }
  .product-name--small { font-size: 44px; }
  .product-name--large { font-size: 76px; letter-spacing: 1px; }
  .net-weight {
    font-family: "Arimo", sans-serif;
    font-size: 14px;
    fill: var(--ink);
  }
</style>
</head>
<body>
<svg class="bag-front" viewBox="0 0 800 1200" xmlns="http://www.w3.org/2000/svg">
  <defs>
    <linearGradient id="sky-top" x1="0" y1="0" x2="1" y2="0">
      <stop offset="0" stop-color="var(--sky-deep)"/>
      <stop offset="0.55" stop-color="var(--sky)"/>
      <stop offset="1" stop-color="var(--sky-light)"/>
    </linearGradient>
    <linearGradient id="field-scene" x1="0" y1="0" x2="1" y2="1">
      <stop offset="0" stop-color="var(--leaf)"/>
      <stop offset="0.45" stop-color="var(--mist)"/>
      <stop offset="1" stop-color="#f4f5f2"/>
    </linearGradient>
    <radialGradient id="cake-stack" cx="0.45" cy="0.5" r="0.6">
      <stop offset="0" stop-color="var(--grain)"/>
      <stop offset="1" stop-color="var(--grain-dark)"/>
    </radialGradient>
    <clipPath id="window-clip">
      <circle cx="490" cy="808" r="84"/>
    </clipPath>
  </defs>

  <!-- top sky band -->
  <rect class="top-band" x="186" y="285" width="428" height="62" fill="url(#sky-top)"/>

  <!-- brand band -->
  <g class="brand-band">
    <rect x="186" y="347" width="428" height="110" fill="var(--tan)"/>
    <rect x="186" y="349" width="428" height="2" fill="var(--tan-line)"/>
    <rect x="186" y="453" width="428" height="2" fill="var(--tan-line)"/>
    <circle cx="400" cy="380" r="30" fill="var(--white)"/>
    <text class="brand-name" x="400" y="446" text-anchor="middle">ORVALE FOODS</text>
  </g>

  <!-- field scene -->
  <rect class="field-scene" x="186" y="457" width="428" height="305" fill="url(#field-scene)"
        role="img" aria-label="Rice stalks with golden grain heads and a small bowl of rice"/>

  <text class="flavor" x="283" y="512">Lightly salted</text>

  <g class="benefits">
    <rect x="490" y="538" width="1" height="132" fill="var(--ink-soft)"/>
    <text class="benefit" x="496" y="549">30 CALORIES PER SLICE</text>
    <text class="benefit" x="496" y="573">NATURAL INGREDIENTS</text>
    <text class="benefit" x="496" y="597">NO TRANS FAT</text>
    <text class="benefit" x="496" y="621">NO PRESERVATIVES</text>
    <text class="benefit" x="496" y="645">NO FOOD COLORS</text>
    <text class="benefit" x="496" y="669">WHOLE GRAIN</text>
  </g>

  <!-- gluten free band -->
  <rect class="claim-band" x="186" y="762" width="428" height="42" fill="var(--band)"/>
  <text class="gluten-free" x="233" y="797">GLUTEN FREE</text>

  <!-- lower sky panel -->
  <rect class="bottom-panel" x="186" y="804" width="428" height="162" fill="url(#sky-top)"/>

  <!-- product window -->
  <g class="product-window">
    <circle cx="490" cy="808" r="88" fill="var(--white)"/>
    <rect x="404" y="722" width="172" height="172" clip-path="url(#window-clip)" fill="url(#cake-stack)"
          role="img" aria-label="Stack of lightly salted rice cakes seen through the bag window"/>
  </g>

  <text class="product-name product-name--small" x="212" y="856">rice</text>
  <text class="product-name product-name--large" x="212" y="924">cakes</text>

  <text class="net-weight" x="436" y="938">NET WT 3.5 OZ {100gr}</text>
</svg>
</body>
</html>
```